Tui Netlink Website

We're looking for a basic website and order form for our stripped down ISP, Tui Netlink.

The front page should be basic with our two plan options - we're open to pretty much any design, but one possibility is an image of New Zealand with two clouds above it (similar to the quick mockup attached).

Clicking on one of the plans will then take the user to a basic order form.

We will also need a contact, about, and support page.

Industry/Entity Type

Isp

```html
<!DOCTYPE html>
<html lang="en">
<head>
<meta charset="utf-8">
<title>Tui Netlink</title>
<link rel="stylesheet" href="https://fonts.googleapis.com/css2?family=Bebas+Neue&family=Open+Sans:wght@400&family=Quicksand:wght@400;500;700&display=swap">
<style>
  :root {
    --teal: #74c8aa;
    --gold: #e2b865;
    --rust: #bf5533;
    --white: #ffffff;
    --sky-top: #eef0da;
    --sky-bottom: #dee0b4;
    --land-shadow: rgba(200, 190, 120, 0.45);
  }
  * { margin: 0; padding: 0; box-sizing: border-box; }
  html, body { width: 1200px; height: 666px; overflow: hidden; }
  body {
    position: relative;
    background: linear-gradient(to bottom, var(--sky-top) 0px, var(--sky-top) 142px, var(--sky-bottom) 440px);
    font-family: "Quicksand", sans-serif;
    color: var(--white);
  }
  .site-header {
    position: absolute; left: 0; top: 0;
    width: 1200px; height: 142px;
    background: var(--teal);
  }
  .brand {
    position: absolute; left: 38px; top: 30px;
    font-family: "Quicksand", sans-serif;
    font-weight: 400;
    font-size: 60px;
    line-height: 80px;
    text-transform: uppercase;
    letter-spacing: 1px;
    color: var(--white);
  }
  .main-nav {
    position: absolute; top: 68px; left: 856px;
    display: flex; gap: 32px;
    font-family: "Open Sans", sans-serif;
    font-size: 16px;
  }
  .main-nav a { color: var(--white); text-decoration: none; }
  .map-area {
    position: absolute; left: 10px; top: 150px;
    width: 1165px; height: 478px;
    background: radial-gradient(ellipse at 50% 55%, var(--white) 0%, var(--white) 55%, rgba(255,255,255,0.85) 75%, rgba(255,255,255,0) 100%);
    border-radius: 40% 60% 45% 55% / 55% 45% 60% 40%;
    filter: drop-shadow(0 0 10px var(--land-shadow));
  }
  .cloud-area {
    position: absolute;
    border-radius: 46%;
  }
  .cloud-area-teal { background: var(--teal); }
  .cloud-area-gold { background: var(--gold); }
  .puff-area {
    position: absolute;
    background: var(--gold);
    border-radius: 50%;
  }
  .plan-speed {
    position: absolute;
    font-size: 44px; font-weight: 400; line-height: 1;
  }
  .plan-price {
    position: absolute;
    font-family: "Bebas Neue", sans-serif;
    font-size: 62px; line-height: 1;
    letter-spacing: 0;
  }
  .tagline {
    position: absolute; left: 529px; top: 332px;
    font-size: 24px; line-height: 32px; font-weight: 500;
  }
  .signup {
    position: absolute;
    width: 141px; height: 38px;
    background: var(--rust);
    border-radius: 4px;
    color: var(--white);
    font-weight: 500; font-size: 15px;
    text-decoration: none;
    display: flex; align-items: center; justify-content: center;
  }
</style>
</head>
<body>
  <header class="site-header">
    <div class="brand">Tui Netlink</div>
    <nav class="main-nav">
      <a href="#">About</a>
      <a href="#">Contact us</a>
      <a href="#">Support</a>
    </nav>
  </header>

  <div class="map-area" role="img" aria-label="Map of New Zealand"></div>

  <div class="cloud-area cloud-area-teal" style="left:93px; top:283px; width:327px; height:212px;" role="img" aria-label="Teal cloud illustration"></div>
  <div class="plan-speed" style="left:168px; top:338px;">30 mbps</div>
  <div class="plan-price" style="left:182px; top:377px;">$95/MO.</div>
  <a class="signup" href="#" style="left:186px; top:507px;">SIGN UP NOW!</a>

  <div class="cloud-area cloud-area-gold" style="left:462px; top:276px; width:306px; height:214px;" role="img" aria-label="Gold cloud illustration"></div>
  <div class="tagline">Pure Broadband.<br>Pure Speed.<br>No Limits.</div>

  <div class="puff-area" style="left:431px; top:408px; width:34px; height:42px;" role="img" aria-label="Small cloud puff"></div>
  <div class="puff-area" style="left:411px; top:449px; width:18px; height:18px;" role="img" aria-label="Small cloud puff"></div>
  <div class="puff-area" style="left:729px; top:265px; width:52px; height:38px;" role="img" aria-label="Small cloud puff"></div>
  <div class="puff-area" style="left:780px; top:299px; width:24px; height:22px;" role="img" aria-label="Small cloud puff"></div>

  <div class="cloud-area cloud-area-teal" style="left:798px; top:286px; width:322px; height:210px;" role="img" aria-label="Teal cloud illustration"></div>
  <div class="plan-speed" style="left:855px; top:340px;">100 mbps</div>
  <div class="plan-price" style="left:886px; top:377px;">$99/MO.</div>
  <a class="signup" href="#" style="left:893px; top:507px;">SIGN UP NOW!</a>
</body>
</html>
```